Label for Refill packaging eco-conscious beauty brand

We need a label for our refill pouch. Velvet Harbor is an unscented conditioner formulated using the finest healthy & pure ingredients, free of chemicals and harmful toxins. As a minimalist beauty brand we are proud to be certified with TQB, Norvamark and Silver Kestrel.

We already have the pouches and an exciting label for our regular bottles.
We choose a kraft brown packing for the refill pouch and would like something minimalist but elegant for the label.

```html
<!DOCTYPE html>
<html lang="en">
<head>
<meta charset="utf-8">
<title>Velvet Harbor – Refill Pouch Label</title>
<link rel="stylesheet" href="https://fonts.googleapis.com/css2?family=Raleway:ital,wght@0,400;0,500;1,400&family=Arimo&display=swap">
<style>
  :root {
    --page: #f5f5f5;
    --label: #866a6f;
    --cream: #ecd3c2;
    --gold: #d9a92a;
  }
  html, body {
    margin: 0;
    padding: 0;
    overflow: hidden;
  }
  body {
    width: 1126px;
    height: 1200px;
    background: var(--page);
    position: relative;
  }
  .label {
    position: absolute;
    left: 200px;
    top: 35px;
    width: 725px;
    height: 1130px;
    color: var(--cream);
    text-align: center;
  }
  .label-shape {
    position: absolute;
    inset: 0;
  }
  .brand {
    position: absolute;
    left: 0;
    right: 0;
    top: 150px;
    display: flex;
    flex-direction: column;
    align-items: center;
    gap: 28px;
  }
  .brand-mark {
    width: 72px;
    height: 72px;
    background: var(--gold);
  }
  .brand-name {
    font-family: "Raleway", sans-serif;
    font-weight: 500;
    font-size: 42px;
    line-height: 1.15;
    letter-spacing: 1px;
    color: #ffffff;
    margin: 0;
  }
  .product-name {
    position: absolute;
    left: 0;
    right: 0;
    top: 490px;
    margin: 0;
    font-family: "Raleway", sans-serif;
    font-weight: 500;
    font-size: 86px;
    line-height: 82px;
  }
  .product-type {
    position: absolute;
    left: 0;
    right: 0;
    top: 752px;
    margin: 0;
    font-family: "Raleway", sans-serif;
    font-weight: 400;
    font-size: 40px;
  }
  .product-type-fr {
    position: absolute;
    left: 0;
    right: 0;
    top: 812px;
    margin: 0;
    font-family: "Raleway", sans-serif;
    font-style: italic;
    font-size: 30px;
    letter-spacing: 0.5px;
  }
  .volume {
    position: absolute;
    left: 30px;
    right: 0;
    top: 962px;
    margin: 0;
    font-family: "Arimo", sans-serif;
    font-size: 32px;
  }
</style>
</head>
<body>
  <section class="label">
    <svg class="label-shape" width="725" height="1130" viewBox="0 0 725 1130" aria-hidden="true">
      <path d="M0 0 H725 V1035 Q362.5 1225 0 1035 Z" fill="var(--label)"/>
    </svg>

    <div class="brand">
      <div class="brand-mark"></div>
      <p class="brand-name">HELDER<br>Mareike</p>
    </div>

    <h1 class="product-name">Velvet<br>Harbor</h1>
    <p class="product-type">unscented hair conditioner</p>
    <p class="product-type-fr">apres-shampoing non parfume</p>
    <p class="volume">238ml e/8ft oz.</p>
  </section>
</body>
</html>
```